Consulting Company Business Card

I am looking for a minimalist, classy, professional design on my business card. I would like it to be double-sided. I want to use the font and color scheme of my logo which are attached. Please be creative in the designs that you send me. I want to play off the design of my logo with the inner C that is Green and Blue broken up with the white.
Target Market(s)
Small Businesses
Industry/Entity Type
Consulting
Contact Information for Business Card
Dale M. Whitcombe, CPA CGMA, 555-014-2873, dwhitcombe@vorantaadvisory.example, www.vorantaadvisory.example

```html
<!DOCTYPE html>
<html lang="en">
<head>
<meta charset="utf-8">
<title>Voranta Advisory — Business Card</title>
<link rel="stylesheet" href="https://fonts.googleapis.com/css2?family=Montserrat:wght@500;700&family=Arimo:wght@400&display=swap">
<style>
  :root {
    --navy: #262f55;
    --teal: #1f7f7c;
    --ink: #1d1d1f;
    --paper: #ffffff;
    --backdrop: #e4e5e8;
    --emblem-light: #e3e8ee;
    --emblem-mid: #c9d3dd;
  }
  * { margin: 0; padding: 0; box-sizing: border-box; }
  html, body {
    width: 1200px;
    height: 901px;
    overflow: hidden;
    background: var(--backdrop);
  }
  .card {
    position: absolute;
    left: 100px;
    top: 165px;
    width: 1000px;
    height: 571px;
    background: var(--paper);
    box-shadow: 0 14px 40px rgba(0,0,0,0.18);
    overflow: hidden;
  }
  .card-edge {
    position: absolute;
    left: 0; right: 0; bottom: 0;
    height: 12px;
    background: var(--navy);
  }
  .emblem-area {
    position: absolute;
    left: 640px;
    top: 55px;
    width: 300px;
    height: 300px;
    border-radius: 50%;
    background: radial-gradient(circle at 40% 40%, var(--emblem-light), var(--emblem-mid));
  }
  .brand {
    position: absolute;
    left: 78px;
    top: 168px;
    display: flex;
    align-items: center;
    gap: 14px;
  }
  .brand-dot {
    width: 20px;
    height: 20px;
    border-radius: 50%;
    background: var(--navy);
  }
  .brand-name {
    font-family: "Montserrat", sans-serif;
    font-weight: 700;
    font-size: 40px;
    letter-spacing: 1px;
    color: var(--navy);
    line-height: 1;
    white-space: nowrap;
  }
  .person {
    position: absolute;
    left: 118px;
    top: 268px;
  }
  .person-name {
    font-family: "Montserrat", sans-serif;
    font-weight: 700;
    font-size: 34px;
    color: var(--navy);
    letter-spacing: 0.5px;
  }
  .person-name .surname { color: var(--teal); }
  .person-title {
    font-family: "Arimo", sans-serif;
    font-size: 22px;
    color: var(--ink);
    margin-top: 2px;
  }
  .contacts {
    position: absolute;
    left: 122px;
    top: 400px;
    list-style: none;
    font-family: "Arimo", sans-serif;
    font-size: 21px;
    color: var(--ink);
  }
  .contacts li {
    display: flex;
    align-items: center;
    gap: 16px;
    height: 34px;
  }
  .contacts svg {
    width: 22px;
    height: 22px;
    flex: none;
    fill: none;
    stroke: var(--navy);
    stroke-width: 1.6;
  }
  .contacts .accent { color: var(--teal); }
</style>
</head>
<body>
  <section class="card" aria-label="Business card">
    <div class="emblem-area" role="img" aria-label="Company emblem goes here"></div>

    <div class="brand">
      <span class="brand-dot"></span>
      <span class="brand-name">VORANTA ADVISORY</span>
    </div>

    <div class="person">
      <h1 class="person-name">Dale M. <span class="surname">Whitcombe</span></h1>
      <p class="person-title">CPA CGMA</p>
    </div>

    <ul class="contacts">
      <li>
        <svg viewBox="0 0 24 24" aria-hidden="true"><path d="M6 3l3 4-2 2c1 3 4 6 7 7l2-2 4 3-2 3c-8 0-15-7-15-15z" fill="var(--navy)" stroke="none"/></svg>
        <span>555-014-2873</span>
      </li>
      <li>
        <svg viewBox="0 0 24 24" aria-hidden="true"><rect x="2" y="5" width="20" height="14"/><path d="M2 5l10 8 10-8M2 19l7-7M22 19l-7-7"/></svg>
        <span>dwhitcombe@vorantaadvisory.example</span>
      </li>
      <li>
        <svg viewBox="0 0 24 24" aria-hidden="true"><circle cx="12" cy="12" r="9"/><ellipse cx="12" cy="12" rx="4" ry="9"/><path d="M3 12h18M5 7h14M5 17h14"/></svg>
        <span>www.<span class="accent">vorantaadvisory</span>.example</span>
      </li>
    </ul>

    <div class="card-edge"></div>
  </section>
</body>
</html>
```